Updated Business Card for Optometry Practice

We're a growing optometry practice that is moving to a beautiful new office and we want to update our business card. We just updated our logo so the new card should reflect the new logo. Our practice continually invests in state of the art instruments to help us provide eye care that is thorough, comfortable, efficient and educational.

I've attached our current card and logo. You can reference this for the information I would like on the card. The tag line on the back is "We're changing the way you see."

Upon completion of this project we will need (amongst other formats) Photoshop files of the card so I can change employee names to print cards for each employee.

```html
<!DOCTYPE html>
<html lang="en">
<head>
<meta charset="utf-8">
<title>Brookfield Family Eyecare – Business Card</title>
<link href="https://fonts.googleapis.com/css2?family=Montserrat:wght@400;500;700;800&display=swap" rel="stylesheet">
<style>
  :root {
    --navy: #13284f;
    --gold: #d8b02f;
    --white: #ffffff;
    --ink: #1a1a1a;
    --backdrop: #d9d9d9;
  }
  * { margin: 0; padding: 0; box-sizing: border-box; }
  html, body { width: 1200px; height: 856px; overflow: hidden; }
  body {
    background: var(--backdrop);
    font-family: "Montserrat", Arial, sans-serif;
    display: flex;
    align-items: center;
    justify-content: center;
    gap: 60px;
  }
  .card {
    position: relative;
    width: 525px;
    height: 300px;
    overflow: hidden;
  }

  /* Front */
  .card-front { background: var(--white); color: var(--navy); }
  .front-brand {
    position: absolute;
    left: 32px;
    top: 70px;
    display: flex;
    align-items: center;
    gap: 10px;
    font-weight: 700;
    font-size: 21px;
    color: var(--navy);
  }
  .brand-dot {
    width: 16px; height: 16px;
    border-radius: 50%;
    background: var(--gold);
    flex: none;
  }
  .person { position: absolute; left: 32px; top: 140px; }
  .person-name { font-weight: 800; font-size: 20px; letter-spacing: 0.2px; }
  .person-name .surname { color: var(--gold); }
  .person-role { color: var(--gold); font-size: 13px; font-weight: 500; margin-top: 2px; }
  .contact { position: absolute; left: 32px; top: 208px; list-style: none; }
  .contact li {
    display: flex; align-items: center; gap: 8px;
    font-size: 12px; color: var(--ink); line-height: 22px;
  }
  .contact svg { width: 13px; height: 13px; fill: var(--navy); flex: none; }
  .address {
    position: absolute;
    right: 32px;
    top: 168px;
    text-align: right;
    font-style: normal;
    font-size: 12.5px;
    line-height: 18px;
    color: var(--ink);
  }
  .address-company { color: var(--gold); font-weight: 700; }

  /* Back */
  .card-back {
    background: var(--navy);
    border-left: 4px solid var(--gold);
    border-bottom: 4px solid var(--gold);
    display: flex;
    align-items: center;
    justify-content: center;
  }
  .back-brand {
    display: flex;
    align-items: center;
    gap: 14px;
    color: var(--white);
    font-weight: 700;
    font-size: 28px;
  }
  .back-brand .brand-dot { width: 22px; height: 22px; }
</style>
</head>
<body>
  <section class="card card-front" aria-label="Business card front">
    <div class="front-brand"><span class="brand-dot"></span>Brookfield Family Eyecare</div>

    <div class="person">
      <p class="person-name">DANIEL <span class="surname">MAREK, OD</span></p>
      <p class="person-role">Optometrist</p>
    </div>

    <ul class="contact">
      <li><svg viewBox="0 0 24 24" aria-hidden="true"><path d="M6.6 10.8a15 15 0 0 0 6.6 6.6l2.2-2.2a1 1 0 0 1 1-.25 11.4 11.4 0 0 0 3.6.57 1 1 0 0 1 1 1V20a1 1 0 0 1-1 1A17 17 0 0 1 3 4a1 1 0 0 1 1-1h3.5a1 1 0 0 1 1 1c0 1.250.2 2.450.57 3.57a1 1 0 0 1-.25 1z"/></svg>(555) 014-2290</li>
      <li><svg viewBox="0 0 24 24" aria-hidden="true"><path d="M2 5h20v14H2zm2 2v.4l8 5 8-5V7l-8 5z"/></svg>dan@brookfieldeyecare.com</li>
      <li><svg viewBox="0 0 24 24" aria-hidden="true"><circle cx="12" cy="12" r="10"/></svg>www.brookfieldeyecare.com</li>
    </ul>

    <address class="address">
      <span class="address-company">Brookfield Family Eyecare</span><br>
      2870 Harlow Park Dr #210<br>
      Brookfield, MO 65901
    </address>
  </section>

  <section class="card card-back" aria-label="Business card back">
    <div class="back-brand"><span class="brand-dot"></span>Brookfield Family Eyecare</div>
  </section>
</body>
</html>
```